Lebel for 500g Honey Jar

We want a design for a 500g honey bottle or Jar as shown in the attached image . All Requirement has been put in the attached brief document .
Also Logo and images have been uploaded . Feel free to play arround with the selected solor schemes .

Target Market(s)

Retail Market

Industry/Entity Type

FMCG

Colors
00AB8E
00BBA5
67D7C9
C6EFE9
E9F9F6
59FF00
82FF00
B8FF75
E3FFCB
F4FFEA
FFC000
F8CF3A
FAE287
FDF2CF
FEFAEE
F0912C
F2A743
F7CA91
FBE8D2
FDF5EE
EE7325
F08F49
F5BC92
FAE3D3
FDF4ED

Requirements
Must have
• The desing must contain the company Address, Logo , and Nutritional Facts
Nice to have
• Image of a honey Bee , see samples attahed

```html
<!DOCTYPE html>
<html lang="en">
<head>
<meta charset="utf-8">
<title>Meadowly Pure Honey – 500g Jar Label</title>
<link href="https://fonts.googleapis.com/css2?family=Fraunces:opsz,wght@9..144,800;9..144,900&family=Lexend:wght@400;600;700&display=swap" rel="stylesheet">
<style>
  :root {
    --backdrop: #5f5f5f;
    --label-white: #ffffff;
    --drip-yellow: #dede08;
    --leaf-green: #93c01f;
    --ink: #1d1d1b;
    --honey-light: #fdf2cf;
    --honey-mid: #fae287;
    --honey-deep: #f7ca91;
    --honey-gold: #f2a743;
  }
  * { margin: 0; padding: 0; box-sizing: border-box; }
  html, body {
    width: 716px; height: 1200px; overflow: hidden;
    background: var(--backdrop);
  }
  .label {
    position: relative;
    width: 716px; height: 1200px;
    font-family: "Lexend", sans-serif;
    color: var(--ink);
  }
  .label-art { position: absolute; inset: 0; width: 716px; height: 1200px; }
  .brand-name {
    position: absolute; left: 0; right: 0; top: 150px;
    text-align: center;
    font-family: "Lexend", sans-serif;
    font-weight: 700; font-size: 84px; letter-spacing: -2px;
    color: var(--ink);
  }
  .product-title {
    position: absolute; left: 0; right: 0; top: 548px;
    text-align: center;
    font-family: "Fraunces", serif;
    font-weight: 900; font-size: 74px; line-height: 1;
    background: linear-gradient(90deg, var(--honey-deep), var(--honey-light) 55%, var(--honey-deep));
    -webkit-background-clip: text; background-clip: text;
    color: transparent;
    filter: drop-shadow(1px 2px 1px rgba(90, 110, 10, 0.45));
  }
  .bee-illustration {
    position: absolute; left: 40px; top: 760px; width: 200px; height: 145px;
    border-radius: 50%;
    background: radial-gradient(ellipse at center, var(--honey-light), var(--honey-deep) 70%, transparent 72%);
  }
  .claim {
    position: absolute;
    font-family: "Fraunces", serif;
    font-weight: 900; font-size: 33px; line-height: 1;
    color: var(--ink);
    white-space: nowrap;
  }
  .claim--additive { left: 276px; top: 722px; }
  .claim--colouring { left: 309px; top: 808px; }
  .claim--preservative { left: 278px; top: 893px; }
  .honeycomb {
    position: absolute; left: 594px; top: 652px; width: 122px; height: 430px;
    border-radius: 24px 0 0 24px;
    background: linear-gradient(160deg, var(--honey-light), var(--honey-deep));
    opacity: 0.9;
  }
  .distributor {
    position: absolute; left: 0; right: 0; top: 990px;
    text-align: center;
    font-size: 31px; font-weight: 400; line-height: 42px;
  }
  .net-weight {
    position: absolute; left: 243px; top: 1112px; width: 231px; height: 100px;
    background: var(--label-white);
    border-radius: 36px 36px 0 0;
    text-align: center;
    padding-top: 28px;
    font-weight: 600; font-size: 24px;
    color: var(--leaf-green);
  }
</style>
</head>
<body>
  <main class="label">
    <svg class="label-art" viewBox="0 0 1000 1676" preserveAspectRatio="none" aria-hidden="true">
      <defs>
        <clipPath id="label-shape">
          <path d="M0,460 C0,200 230,0 500,0 C770,0 1000,200 1000,460 L1000,1576 Q1000,1676 900,1676 L100,1676 Q0,1676 0,1576 Z"/>
        </clipPath>
        <linearGradient id="arc-gold" x1="0" y1="0" x2="0" y2="1">
          <stop offset="0" stop-color="#f7ca91"/>
          <stop offset="0.5" stop-color="#fdf2cf"/>
          <stop offset="1" stop-color="#f2a743"/>
        </linearGradient>
      </defs>
      <g clip-path="url(#label-shape)">
        <rect class="label-top" width="1000" height="1676" fill="var(--label-white)"/>
        <path class="drip-band" fill="var(--drip-yellow)"
          d="M0,620 C60,640 90,560 110,520 C140,460 200,440 260,450 C330,460 380,510 410,500 C440,490 440,445 470,450 C510,455 530,530 560,580 C600,650 640,600 690,560 C730,530 770,520 800,540 C850,570 900,560 930,510 C960,460 1000,440 1000,440 L1000,1676 L0,1676 Z"/>
        <path class="green-field" fill="var(--leaf-green)"
          d="M0,750 C30,760 90,730 120,640 C150,560 200,520 260,530 C330,540 350,580 400,590 C440,600 470,560 500,570 C560,590 580,700 640,700 C690,700 710,620 750,600 C800,580 860,630 900,620 C950,600 980,530 1000,510 L1000,1676 L0,1676 Z"/>
        <path class="bee-arc" d="M118,993 A180,168 0 1 1 145,1332" fill="none" stroke="url(#arc-gold)" stroke-width="10" stroke-linecap="round"/>
      </g>
    </svg>

    <div class="brand-name">Meadowly</div>

    <h1 class="product-title">Pure Honey</h1>

    <div class="bee-illustration" role="img" aria-label="Illustration of a smiling honey bee with spread wings"></div>

    <p class="claim claim--additive">Zero additive</p>
    <p class="claim claim--colouring">Zero colouring</p>
    <p class="claim claim--preservative">Zero preservative</p>

    <div class="honeycomb" role="img" aria-label="Decorative honeycomb cells along the right edge"></div>

    <p class="distributor">Packed &amp; Distributed by<br>Fieldbloom Farms Limited</p>

    <div class="net-weight">Net WT: 500g</div>
  </main>
</body>
</html>
```